Brenton High 20 year Reunion Memorial

I need a tasteful memorial poster with the names of those alumni that have deceased. The school colors are black, orange, silver and white. I would definately like the background to be black. At the top of the poster I would like it to read:
Brenton Hight School Class of 1993.
This evening is dedicated in memory of
(followed by the names on the attached file

Industry/Entity Type

School

Requirements
Must have
• Black background

```html
<!DOCTYPE html>
<html lang="en">
<head>
<meta charset="utf-8">
<title>Brenton High School Class of 1993 – In Memory</title>
<link rel="stylesheet" href="https://fonts.googleapis.com/css2?family=Cinzel:wght@400;500&display=swap">
<style>
  :root {
    --bg: #000000;
    --ink: #f2f2f2;
    --ink-soft: #d9d9d9;
    --rule: #e6e6e6;
    --ornament: #2a2a2a;
  }
  * { margin: 0; padding: 0; box-sizing: border-box; }
  html, body {
    width: 848px;
    height: 1200px;
    overflow: hidden;
    background: var(--bg);
  }
  .poster {
    position: relative;
    width: 848px;
    height: 1200px;
    background: var(--bg);
    color: var(--ink);
    font-family: "Cinzel", "Trajan Pro", serif;
  }
  .poster__title {
    position: absolute;
    top: 74px;
    left: 0;
    width: 100%;
    text-align: center;
    font-weight: 400;
    font-size: 56px;
    line-height: 66px;
    letter-spacing: 1px;
    font-variant: small-caps;
  }
  .divider {
    position: absolute;
    left: 107px;
    width: 634px;
    height: 40px;
  }
  .divider--top { top: 226px; }
  .divider--bottom { top: 996px; }
  .divider__rule {
    position: absolute;
    top: 20px;
    height: 1.5px;
    width: 262px;
    background: var(--rule);
  }
  .divider__rule--left { left: 0; }
  .divider__rule--right { right: 0; }
  .divider__flourish {
    position: absolute;
    left: 270px;
    top: 6px;
    width: 94px;
    height: 28px;
  }
  .poster__dedication {
    position: absolute;
    top: 322px;
    left: 0;
    width: 100%;
    text-align: center;
    font-weight: 400;
    font-size: 38px;
    line-height: 50px;
    letter-spacing: 1px;
    font-variant: small-caps;
  }
  .memorial-list {
    position: absolute;
    top: 462px;
    left: 0;
    width: 100%;
    list-style: none;
  }
  .memorial-list__entry {
    display: flex;
    align-items: baseline;
    height: 68.5px;
  }
  .memorial-list__name {
    width: 327px;
    text-align: right;
    font-size: 28px;
    letter-spacing: 0.5px;
    color: var(--ink);
  }
  .memorial-list__dates {
    margin-left: 24px;
    font-size: 21px;
    letter-spacing: 0.3px;
    color: var(--ink-soft);
  }
</style>
</head>
<body>
<main class="poster">
  <h1 class="poster__title">Brenton High School<br>Class of 1993</h1>

  <div class="divider divider--top">
    <span class="divider__rule divider__rule--left"></span>
    <svg class="divider__flourish" role="img" aria-label="Decorative scroll flourish" viewBox="0 0 94 28">
      <ellipse cx="47" cy="14" rx="45" ry="12" fill="var(--ornament)"/>
    </svg>
    <span class="divider__rule divider__rule--right"></span>
  </div>

  <h2 class="poster__dedication">This evening is dedicated<br>in memory of</h2>

  <ul class="memorial-list">
    <li class="memorial-list__entry"><span class="memorial-list__name">Carla Jensen</span><span class="memorial-list__dates">May 7, 1975-November 28, 1993</span></li>
    <li class="memorial-list__entry"><span class="memorial-list__name">Derek Hale</span><span class="memorial-list__dates">April 29, 1975-June 10, 1997</span></li>
    <li class="memorial-list__entry"><span class="memorial-list__name">Scott Rainer</span><span class="memorial-list__dates">April 22, 1975- April 2, 2002</span></li>
    <li class="memorial-list__entry"><span class="memorial-list__name">Paul Moreno</span><span class="memorial-list__dates">August 28, 1975-February 27, 2010</span></li>
    <li class="memorial-list__entry"><span class="memorial-list__name">Kerri Lindqvist</span><span class="memorial-list__dates">July 13, 1975-October 5, 2011</span></li>
    <li class="memorial-list__entry"><span class="memorial-list__name">Holly Bennett</span><span class="memorial-list__dates">January 26, 1975-December 22, 2012</span></li>
    <li class="memorial-list__entry"><span class="memorial-list__name">Casey Dorran</span><span class="memorial-list__dates">April 29, 1975- January 30, 2013</span></li>
  </ul>

  <div class="divider divider--bottom">
    <span class="divider__rule divider__rule--left"></span>
    <svg class="divider__flourish" role="img" aria-label="Decorative scroll flourish" viewBox="0 0 94 28">
      <ellipse cx="47" cy="14" rx="45" ry="12" fill="var(--ornament)"/>
    </svg>
    <span class="divider__rule divider__rule--right"></span>
  </div>
</main>
</body>
</html>
```